Potato chips bag design of 85 gram for Greek and East Europe market

I want a new design for a new potato chips bag for the Greek market. The product is going to be all natural ingredient, gluten free, preservatives free, allergen free from Greek organic potatoes . Thick cut, marinated potatoes that are premium vs others. For packaging we want it to stand out on shelf. Have a Matt film . It will be called Silverbrook Tumble. Salt and Oregano flavors to start with.
Ideally to stand out on shelf we were thinking to have a black/white Color pallet and have an artistic pattern printed like the pictures attached. But of course open to ideas.
Target Market(s)
Greece and East Europe
Industry/Entity Type
Snacks Packaged goods
Requirements
Must have
- Matt film that stands out on shelf . 85 grams bag so 25cm tall and 15 cms length
Nice to have
- Ideally black/white pallet as it looks more premium. Patterns artistic that will make it look like art.
Should not have
- Traditional Pevo type of design (red-green colors etc)

```html
<!DOCTYPE html>
<html lang="en">
<head>
<meta charset="UTF-8">
<title>Silverbrook Tumble – Salt &amp; Oregano 85 gr.</title>
<link rel="stylesheet" href="https://fonts.googleapis.com/css2?family=Chakra+Petch:wght@700&family=Poppins:wght@400;500&display=swap">
<style>
  :root {
    --ink: #000000;
    --paper: #ffffff;
    --engrave-light: #b4b4b4;
    --engrave-mid: #7a7a7a;
    --engrave-dark: #3a3a3a;
  }
  * { margin: 0; padding: 0; box-sizing: border-box; }
  html, body {
    width: 960px;
    height: 1200px;
    overflow: hidden;
    background: var(--ink);
  }
  .bag-front {
    position: relative;
    width: 960px;
    height: 1200px;
    background: var(--ink);
    overflow: hidden;
    color: var(--paper);
  }
  .artwork {
    position: absolute;
    border-radius: 50%;
    background: radial-gradient(closest-side, var(--engrave-light), var(--engrave-mid) 45%, var(--engrave-dark) 78%, transparent 100%);
  }
  .artwork--herbs-top-left   { left: -60px;  top: -60px;  width: 560px; height: 440px; }
  .artwork--herbs-top-right  { left: 440px;  top: -60px;  width: 360px; height: 190px; }
  .artwork--herb-edge-right  { left: 820px;  top: -40px;  width: 200px; height: 280px; }
  .artwork--sprig-centre     { left: 200px;  top: 150px;  width: 700px; height: 560px; }
  .artwork--sprig-left       { left: -40px;  top: 400px;  width: 240px; height: 200px; }
  .artwork--sprig-right      { left: 790px;  top: 330px;  width: 220px; height: 240px; }
  .artwork--potatoes-left    { left: -40px;  top: 610px;  width: 280px; height: 290px; }
  .artwork--potato-right     { left: 880px;  top: 630px;  width: 140px; height: 200px; }
  .artwork--stem-centre      { left: 320px;  top: 740px;  width: 360px; height: 260px; }
  .artwork--salt-spoon       { left: 610px;  top: 800px;  width: 320px; height: 260px; }
  .artwork--herbs-bottom-left  { left: -60px; top: 880px;  width: 560px; height: 400px; }
  .artwork--herbs-bottom-right { left: 720px; top: 1000px; width: 300px; height: 260px; }

  .title {
    position: absolute;
    left: 0;
    right: 0;
    top: 460px;
    display: flex;
    flex-direction: column;
    align-items: center;
    gap: 8px;
    font-family: "Chakra Petch", sans-serif;
    font-weight: 700;
    text-transform: uppercase;
    line-height: 1;
  }
  .title-line {
    background: var(--ink);
    padding: 8px 16px 4px;
    font-size: 94px;
    letter-spacing: 1px;
  }
  .flavour {
    position: absolute;
    left: 214px;
    top: 695px;
    width: 535px;
    height: 65px;
    border-radius: 12px;
    background: var(--ink);
    display: flex;
    align-items: center;
    justify-content: center;
    font-family: "Poppins", sans-serif;
    font-weight: 400;
    font-size: 39px;
  }
  .claims {
    position: absolute;
    left: 0;
    right: 0;
    top: 808px;
    list-style: none;
    text-align: center;
    font-family: "Poppins", sans-serif;
    font-weight: 500;
    font-size: 24px;
    line-height: 30.5px;
    text-shadow:
      -2px -2px 0 var(--ink), 2px -2px 0 var(--ink),
      -2px 2px 0 var(--ink), 2px 2px 0 var(--ink),
      0 0 6px var(--ink);
  }
  .weight {
    position: absolute;
    left: 0;
    right: 0;
    top: 1068px;
    text-align: center;
    font-family: "Chakra Petch", sans-serif;
    font-weight: 700;
    font-size: 44px;
    letter-spacing: 3px;
    text-shadow: 0 0 8px var(--ink);
  }
</style>
</head>
<body>
  <main class="bag-front">
    <div class="artwork artwork--herbs-top-left" role="img" aria-label="Engraved oregano leaves, top left"></div>
    <div class="artwork artwork--herbs-top-right" role="img" aria-label="Engraved oregano sprig, top"></div>
    <div class="artwork artwork--herb-edge-right" role="img" aria-label="Engraved oregano leaves, top right edge"></div>
    <div class="artwork artwork--sprig-centre" role="img" aria-label="Large engraved oregano bunch behind the title"></div>
    <div class="artwork artwork--sprig-left" role="img" aria-label="Engraved oregano sprig, left"></div>
    <div class="artwork artwork--sprig-right" role="img" aria-label="Engraved oregano sprig, right"></div>
    <div class="artwork artwork--potatoes-left" role="img" aria-label="Engraved cut potatoes, left"></div>
    <div class="artwork artwork--potato-right" role="img" aria-label="Engraved halved potato, right edge"></div>
    <div class="artwork artwork--stem-centre" role="img" aria-label="Engraved oregano stems behind the claims"></div>
    <div class="artwork artwork--salt-spoon" role="img" aria-label="Engraved wooden spoon of sea salt with scattered crystals"></div>
    <div class="artwork artwork--herbs-bottom-left" role="img" aria-label="Engraved oregano bunch, bottom left"></div>
    <div class="artwork artwork--herbs-bottom-right" role="img" aria-label="Engraved oregano leaves, bottom right"></div>

    <h1 class="title">
      <span class="title-line">Silverbrook</span>
      <span class="title-line">Tumble</span>
    </h1>

    <p class="flavour">Salt &amp; Oregano</p>

    <ul class="claims">
      <li>all natural ingredient</li>
      <li>gluten free</li>
      <li>preservatives free</li>
      <li>allergen free</li>
      <li>Greek organic potatoes</li>
    </ul>

    <p class="weight">85 GR.</p>
  </main>
</body>
</html>
```